Halvern Partners M&A Email Newsletter Design

Halvern Partners is a Marketing/Consulting/M&A company and we want to find a graphic designer experienced in newsletter design. Please visit our website for more information and to see our logo. We would like the color scheme of the newsletter to reflect our colors of blue, yellow, and dark gray (see website for visual representation). The newsletter will focus on detailing M&A news in the market. Please reach out if you have any questions. https://www.halvernpartners-example.net/

Marketing

Font styles to use
Serif
Sans Serif

Colors
0456a4
ffc214
ffcf3e

Requirements
Must have
• Halvern Partners' Color Scheme: Yellow, Blue, Dark Gray (see website)
Professional economics newsletter
Should not have
• Strange/hard to read fonts

```html
<!DOCTYPE html>
<html lang="en">
<head>
<meta charset="utf-8">
<title>Halvern Partners – M&amp;A News</title>
<link rel="stylesheet" href="https://fonts.googleapis.com/css2?family=Mulish:wght@400;600;700;800;900&display=swap">
<style>
  :root {
    --frame: #111111;
    --header-bg: #e8e8e8;
    --yellow: #f2c614;
    --yellow-light: #f6d443;
    --yellow-deep: #d9ad0c;
    --blue: #0a36f0;
    --ink: #3c3c3c;
    --text-gray: #555555;
    --muted: #777777;
    --panel-bg: #ececec;
    --footer-bg: #222222;
    --white: #ffffff;
  }
  * { box-sizing: border-box; margin: 0; padding: 0; }
  html, body {
    width: 1200px; height: 3435px; overflow: hidden;
    background: var(--frame);
    font-family: "Mulish", Arial, sans-serif;
  }
  .newsletter {
    position: absolute; left: 23px; top: 23px;
    width: 1149px; height: 3389px;
    background: var(--white);
    overflow: hidden;
  }
  .abs { position: absolute; }

  /* Header */
  .masthead { left: 0; top: 0; width: 1149px; height: 240px; background: var(--header-bg); }
  .brand {
    left: 50px; top: 90px;
    font-size: 54px; font-weight: 800; color: var(--ink); line-height: 1;
  }
  .issue-tab { right: 0; top: 73px; width: 430px; height: 110px; }
  .issue-tab span {
    position: absolute; inset: 0; display: flex; align-items: center; justify-content: center;
    padding-left: 30px;
    font-size: 50px; font-weight: 900; color: var(--white);
  }

  /* Hero */
  .hero {
    left: 0; top: 240px; width: 1149px; height: 561px;
    background: radial-gradient(ellipse at 50% 55%, var(--yellow-light) 0%, var(--yellow) 55%, var(--yellow-deep) 100%);
  }
  .hero-title {
    position: absolute; left: 0; right: 0; top: 240px;
    text-align: center; color: var(--white);
    font-size: 50px; font-weight: 900; line-height: 68px; text-transform: uppercase;
  }

  /* Intro */
  .intro {
    left: 50px; top: 882px; width: 1040px;
    font-size: 34px; line-height: 50px; color: var(--text-gray);
  }
  .section-title {
    left: 50px; top: 1118px;
    font-size: 48px; font-weight: 900; color: var(--blue); text-transform: uppercase;
  }

  /* Service rows */
  .service { left: 48px; width: 1070px; height: 318px; }
  .service-photo { position: absolute; left: 0; top: 0; width: 524px; height: 318px; }
  .photo-start { background: linear-gradient(180deg, #6e6e6e 0%, #2f2f2f 60%, #4a4a4a 100%); }
  .photo-compass { background: linear-gradient(135deg, #f1f1f1 0%, #c9ced3 55%, #8fa8c6 100%); }
  .photo-handshake { background: linear-gradient(90deg, #3a3a44 0%, #c8ccd2 45%, #eef0f2 100%); }
  .photo-esop { background: linear-gradient(90deg, #f2e700 0%, #f2e700 9%, #bcd0e8 9%, #5d8fc8 100%); }
  .service-card {
    position: absolute; left: 472px; top: 25px; width: 590px; height: 270px;
    background: var(--blue); color: var(--white);
    padding: 62px 30px 0 36px;
  }
  .service-card h3 { font-size: 30px; font-weight: 800; white-space: nowrap; }
  .service-card p { margin-top: 20px; max-width: 480px; font-size: 20.5px; line-height: 34px; font-weight: 600; }

  /* Closing panel */
  .closing { left: 0; top: 2784px; width: 1149px; height: 484px; background: var(--panel-bg); }
  .closing-ring {
    position: absolute; left: 126px; top: 96px; width: 302px; height: 302px;
    border-radius: 50%; border: 3px solid #b9c6f0; padding: 8px;
  }
  .closing-photo {
    width: 100%; height: 100%; border-radius: 50%;
    background: linear-gradient(180deg, #1f6fa8 0%, #3c93c4 60%, #a9d2e6 100%);
  }
  .chat-icon { position: absolute; left: 530px; top: 98px; }
  .closing-title {
    position: absolute; left: 647px; top: 92px; width: 440px;
    font-size: 32px; line-height: 45px; font-weight: 600; color: var(--blue);
  }
  .closing-body {
    position: absolute; left: 652px; top: 220px; width: 440px;
    font-size: 20px; line-height: 37px; color: var(--muted);
  }

  /* Legal footer */
  .legal {
    left: 0; top: 3268px; width: 1149px; height: 121px; background: var(--footer-bg);
    display: flex; align-items: center; justify-content: center;
    text-align: center; color: var(--white);
    font-size: 20px; line-height: 34px; font-weight: 700;
  }
</style>
</head>
<body>
<main class="newsletter">

  <header class="abs masthead">
    <div class="abs brand">Halvern Partners</div>
    <div class="abs issue-tab">
      <svg width="430" height="110" viewBox="0 0 430 110" aria-hidden="true">
        <polygon points="22,0 430,0 430,110 22,110 0,55" fill="var(--blue)"/>
      </svg>
      <span>M&amp;A NEWS</span>
    </div>
  </header>

  <section class="abs hero" role="img" aria-label="Team of hands stacked together in a circle, tinted yellow">
    <h1 class="hero-title">Helping agency owners<br>achieve their life’s ambitions.</h1>
  </section>

  <p class="abs intro">We use proprietary methodologies executed by former owners and CEOs of marketing communications agencies to help you achieve your goals.</p>

  <h2 class="abs section-title">M&amp;A Transactions</h2>

  <article class="abs service" style="top:1216px">
    <div class="service-photo photo-start" role="img" aria-label="Runner crouched at a starting line marked 2020"></div>
    <div class="service-card">
      <h3>SALES READINESS ASSESSMENT</h3>
      <p>Make sure your agency is firing on all cylinders at the time of sale to maximize your current value and any potential earnout.</p>
    </div>
  </article>

  <article class="abs service" style="top:1605px">
    <div class="service-photo photo-compass" role="img" aria-label="Compass needle pointing toward the word success"></div>
    <div class="service-card">
      <h3>SALES READINESS ASSESSMENT</h3>
      <p>Make sure your agency is firing on all cylinders at the time of sale to maximize your current value and any potential earnout.</p>
    </div>
  </article>

  <article class="abs service" style="top:1985px">
    <div class="service-photo photo-handshake" role="img" aria-label="Two business people shaking hands"></div>
    <div class="service-card">
      <h3>SALES READINESS ASSESSMENT</h3>
      <p>Make sure your agency is firing on all cylinders at the time of sale to maximize your current value and any potential earnout.</p>
    </div>
  </article>

  <article class="abs service" style="top:2368px">
    <div class="service-photo photo-esop" role="img" aria-label="Employee Stock Ownership Plan lettering over financial figures"></div>
    <div class="service-card">
      <h3>SALES READINESS ASSESSMENT</h3>
      <p>Make sure your agency is firing on all cylinders at the time of sale to maximize your current value and any potential earnout.</p>
    </div>
  </article>

  <section class="abs closing">
    <div class="closing-ring">
      <div class="closing-photo" role="img" aria-label="Hand reaching for a red ladder against a blue sky"></div>
    </div>
    <svg class="chat-icon" width="92" height="86" viewBox="0 0 92 86" aria-hidden="true">
      <path d="M10 4 H82 a6 6 0 0 1 6 6 V54 a6 6 0 0 1 -6 6 H40 L22 80 V60 H10 a6 6 0 0 1 -6 -6 V10 a6 6 0 0 1 6 -6 Z"
            fill="none" stroke="var(--blue)" stroke-width="5" stroke-linejoin="round"/>
      <circle cx="30" cy="32" r="5" fill="var(--blue)"/>
      <circle cx="46" cy="32" r="5" fill="var(--blue)"/>
      <circle cx="62" cy="32" r="5" fill="var(--blue)"/>
    </svg>
    <h2 class="closing-title">We help you maximize your agency's success.</h2>
    <p class="closing-body">We use proven, proprietary methodologies implemented by former agency owners and operators who have sat in your chair, understand your challenges and successfully built and sold their agencies.</p>
  </section>

  <footer class="abs legal">
    <p>© 2020 Halvern Partners Consultancy, LLC. All Content is property of<br>Halvern Partners Consultancy, LLC. All Rights Reserved</p>
  </footer>

</main>
</body>
</html>
```